Business Card Design

we need a bussiness card for the transport company called Harvel Transport
name of contact person that should display on card is Mankirat Sekhon contact no 0478162093
we do the dry goods and frozen deliveries in melbourne every day
happy to beat any quote

Business

Contact Information for Business Card

Harvel transport
Mankirat sekhon
mob 0478162093
contact us for any refrigerator or dry goods delivery
deliver all over melbourne

```html
<!DOCTYPE html>
<html lang="en">
<head>
<meta charset="UTF-8">
<title>Harvel Transport – Business Card</title>
<link href="https://fonts.googleapis.com/css2?family=Arimo:wght@400;700&family=Cinzel:wght@700&display=swap" rel="stylesheet">
<style>
  :root {
    --page-bg: #e6e3df;
    --card-bg: #ffffff;
    --brand-red: #9b2a22;
    --accent-red: #b3231c;
    --ink: #1c1c1c;
    --body-ink: #333333;
    --rule-grey: #7a7a7a;
    --card-shadow: rgba(0, 0, 0, 0.18);
  }
  * { box-sizing: border-box; margin: 0; padding: 0; }
  html, body {
    width: 1200px;
    height: 1200px;
    overflow: hidden;
    background: var(--page-bg);
  }
  .sheet {
    position: relative;
    width: 1200px;
    height: 1200px;
  }
  .card {
    position: absolute;
    left: 150px;
    width: 900px;
    height: 540px;
    background: var(--card-bg);
    box-shadow: 0 6px 20px var(--card-shadow);
  }
  .card--front { top: 40px; }
  .card--back { top: 620px; }

  .brand-name {
    font-family: "Arimo", Arial, sans-serif;
    font-weight: 400;
    color: var(--brand-red);
    text-align: center;
    line-height: 1.1;
  }
  .brand-name__main {
    display: block;
    font-size: 66px;
    letter-spacing: 1px;
  }
  .brand-name__sub {
    display: block;
    font-size: 46px;
    letter-spacing: 1px;
    margin-top: 6px;
  }

  .card--front .brand-name {
    position: absolute;
    left: 30px;
    width: 340px;
    top: 200px;
  }
  .card--front .brand-name__main { font-size: 58px; }
  .card--front .brand-name__sub { font-size: 40px; }

  .divider {
    position: absolute;
    left: 395px;
    top: 90px;
    width: 3px;
    height: 360px;
    background: var(--brand-red);
  }

  .contact {
    position: absolute;
    left: 440px;
    top: 110px;
    width: 400px;
  }
  .contact__name {
    font-family: "Cinzel", "Times New Roman", serif;
    font-weight: 700;
    font-size: 29px;
    letter-spacing: 1.5px;
    color: var(--ink);
    text-transform: uppercase;
    padding-bottom: 6px;
    border-bottom: 1.5px solid var(--rule-grey);
    text-align: center;
  }
  .contact__phone {
    font-family: "Arimo", Arial, sans-serif;
    font-weight: 700;
    font-size: 24px;
    padding: 10px 0 8px 14px;
    border-bottom: 1.5px solid var(--rule-grey);
    white-space: nowrap;
  }
  .contact__phone-label { color: var(--accent-red); }
  .contact__phone-number { color: var(--ink); letter-spacing: 1px; margin-left: 8px; }
  .contact__note {
    font-family: "Arimo", Arial, sans-serif;
    font-weight: 400;
    font-size: 21px;
    line-height: 1.35;
    color: var(--body-ink);
    text-align: center;
    margin-top: 12px;
  }

  .card--back .brand-name {
    position: absolute;
    left: 0;
    right: 0;
    top: 190px;
  }
</style>
</head>
<body>
  <main class="sheet">
    <section class="card card--front" aria-label="Business card front">
      <h1 class="brand-name">
        <span class="brand-name__main">HARVEL</span>
        <span class="brand-name__sub">TRANSPORT</span>
      </h1>
      <div class="divider"></div>
      <div class="contact">
        <p class="contact__name">Mankirat Sekhon</p>
        <p class="contact__phone">
          <span class="contact__phone-label">MOBILE NO :</span>
          <span class="contact__phone-number">0478162093</span>
        </p>
        <p class="contact__note">contact us for any refrigerator or dry goods delivery deliver all over melbourne.</p>
      </div>
    </section>

    <section class="card card--back" aria-label="Business card back">
      <h2 class="brand-name">
        <span class="brand-name__main">HARVEL</span>
        <span class="brand-name__sub">TRANSPORT</span>
      </h2>
    </section>
  </main>
</body>
</html>
```